Wired Earphone Creative Packaging Design

We would like a creative window box style packaging design for our wired earphone

Size: 6” x 3.5” x 1.5” (enclosed die-cut drawing)
Material: E Flute Paper box
Type: Window Box style
Design features we prefer: friendly, playful, creative, trendy, unique, High tech.
Competitors: Enclosed
Requirement:AI file is preferred

Enclosed are product pictures, marketing materials and competitor designs for your reference.

Any further questions, please feel free to ask.
Updates

So designers get more time to design

Target Market(s)

13-40 Year Olds

Industry/Entity Type

Audio

Colors

Designer to choose colors to be used in the design.

Requirements
Must have
• Window, selling point, creative

```html
<!DOCTYPE html>
<html lang="en">
<head>
<meta charset="utf-8">
<title>SC-1 In-Ear Earphones – Window Box Dieline</title>
<link rel="stylesheet" href="https://fonts.googleapis.com/css2?family=Anton&family=Poppins:wght@600;700&family=Titillium+Web:ital,wght@0,300;0,400;1,300;1,400&display=swap">
<style>
  :root {
    --flap-grey: #818286;
    --panel-grey: #e4e4e4;
    --band-grey: #f2f2f2;
    --window-white: #ffffff;
    --accent-yellow: #f3cd2a;
    --ink-dark: #2b2b2b;
    --ink-black: #111111;
    --spec-text: #b3b4b7;
  }
  html, body { margin: 0; padding: 0; overflow: hidden; background: #ffffff; }
  .dieline { display: block; width: 1200px; height: 1200px; }
  .flap { fill: var(--flap-grey); }
  .tuck-tab { fill: var(--accent-yellow); }
  .main-panel { fill: var(--panel-grey); }
  .base-band { fill: var(--band-grey); }
  .window { fill: var(--window-white); }
  .slot { fill: #ffffff; }
  .subtitle { font-family: "Titillium Web", sans-serif; font-style: italic; font-size: 25px; fill: var(--ink-dark); }
  .headline { font-family: "Anton", sans-serif; font-size: 58px; }
  .headline .accent { fill: var(--accent-yellow); }
  .headline .dark { fill: var(--ink-dark); }
  .feature-line { font-family: "Titillium Web", sans-serif; font-size: 14.5px; fill: var(--ink-dark); text-anchor: middle; }
  .feature-line.accent { fill: var(--accent-yellow); font-weight: 300; }
  .vertical-slogan { font-family: "Anton", sans-serif; font-size: 45px; fill: var(--accent-yellow); letter-spacing: 0.5px; }
  .tag-label { font-family: "Titillium Web", sans-serif; font-size: 18.5px; fill: #ffffff; }
  .callout { font-family: "Titillium Web", sans-serif; font-size: 7.5px; fill: var(--accent-yellow); }
  .leader { stroke: var(--accent-yellow); stroke-width: 0.7; stroke-dasharray: 2 1.5; fill: none; }
  .spec-box { fill: var(--flap-grey); }
  .spec-heading { font-family: "Titillium Web", sans-serif; font-size: 14px; fill: #f1f1f1; }
  .spec-item { font-family: "Titillium Web", sans-serif; font-style: italic; font-weight: 300; font-size: 13.5px; fill: var(--spec-text); }
  .model-number { font-family: "Poppins", sans-serif; font-weight: 700; font-size: 19px; fill: var(--ink-black); }
  .platform-name { font-family: "Poppins", sans-serif; font-weight: 700; font-size: 13px; fill: var(--ink-black); text-anchor: middle; }
</style>
</head>
<body>
<svg class="dieline" viewBox="0 0 1200 1200" xmlns="http://www.w3.org/2000/svg">

  <!-- top closure -->
  <path class="tuck-tab" d="M238 74 V40 Q238 0 278 0 H594 Q634 0 634 40 V74 Z"/>
  <rect class="flap" x="238" y="74" width="396" height="188"/>
  <polygon class="flap" points="80,100 232,100 238,262 68,262"/>
  <polygon class="flap" points="641,100 792,100 804,262 634,262"/>

  <!-- glue flap -->
  <polygon class="flap" points="0,280 68,262 68,1012 0,996"/>

  <!-- main panels -->
  <rect class="main-panel" x="68" y="262" width="1132" height="750"/>
  <rect class="base-band" x="238" y="906" width="962" height="106"/>

  <!-- bottom flaps -->
  <path class="flap" d="M74 1012 H232 V1200 H114 Q74 1200 74 1160 Z"/>
  <rect class="slot" x="142" y="1096" width="22" height="104" rx="11"/>
  <rect class="flap" x="238" y="1012" width="396" height="188"/>
  <rect class="slot" x="306" y="1093" width="259" height="27" rx="10"/>
  <path class="flap" d="M641 1012 H798 V1160 Q798 1200 758 1200 H641 Z"/>
  <rect class="slot" x="709" y="1096" width="22" height="104" rx="11"/>
  <rect class="flap" x="804" y="1012" width="396" height="188"/>
  <rect class="slot" x="872" y="1093" width="259" height="27" rx="10"/>

  <!-- front panel -->
  <g class="front-panel">
    <text class="subtitle" x="282" y="303">Customizable Stereo</text>
    <text class="headline" x="281" y="359" textLength="310" lengthAdjust="spacingAndGlyphs"><tspan class="accent">In- Ear </tspan><tspan class="dark">Earphones</tspan></text>

    <rect x="238" y="394" width="38" height="40" rx="8" fill="#d9d9d9" role="img" aria-label="Product render of a white earbud"/>
    <rect x="294" y="394" width="38" height="40" rx="8" fill="#d9d9d9" role="img" aria-label="Product render of a white earbud"/>
    <rect x="531" y="394" width="38" height="40" rx="8" fill="#d9d9d9" role="img" aria-label="Product render of a white earbud"/>
    <rect x="588" y="394" width="38" height="40" rx="8" fill="#d9d9d9" role="img" aria-label="Product render of a white earbud"/>

    <text class="feature-line" x="423" y="401">Customizable earbuds</text>
    <text class="feature-line accent" x="423" y="419">Silicone Gel Ear tips</text>
    <text class="feature-line" x="429" y="437">Line Mic With 3.5mm Jack</text>

    <rect class="window" x="169" y="468" width="396" height="437"/>

    <text class="vertical-slogan" transform="translate(619 855) rotate(-90)">ERGONOMIC DESIGN</text>
  </g>

  <!-- side panel -->
  <g class="side-panel">
    <path d="M805 270 H1030 Q1040 270 1040 280 V304 Q1040 314 1030 314 H805 Z" fill="var(--accent-yellow)"/>
    <text class="tag-label" x="809" y="298">Customisable and Ergonomic</text>

    <rect x="805" y="330" width="195" height="180" rx="6" fill="#dedede" role="img" aria-label="Product render of earbuds with interchangeable decorative caps"/>
    <rect x="1076" y="288" width="112" height="184" rx="6" fill="#dcdcdc" role="img" aria-label="Product render of a pair of earbuds hanging from their cords"/>

    <text class="callout" x="1005" y="337">Ergonomic design</text>
    <path class="leader" d="M918 335 H1002"/>
    <text class="callout" x="1005" y="369">Good grip</text>
    <path class="leader" d="M945 367 H1002"/>
    <text class="callout" x="1005" y="403">Customizable design</text>
    <path class="leader" d="M975 401 H1002"/>

    <path d="M966 477 H1200 V522 H976 Q966 522 966 512 V487 Q966 477 976 477 Z" fill="var(--flap-grey)"/>
    <text class="tag-label" x="979" y="506">Multifunctional Controller</text>

    <rect x="832" y="540" width="184" height="110" rx="6" fill="#dedede" role="img" aria-label="Product render of the in-line remote controller with yellow volume keys"/>
    <text class="callout" x="1075" y="548">Multifunction key</text>
    <path class="leader" d="M928 545 H1072"/>
    <text class="callout" x="1075" y="581">Volume-up control key</text>
    <path class="leader" d="M990 578 H1072"/>
    <text class="callout" x="1075" y="617">Clothing Clip</text>
    <path class="leader" d="M1000 614 H1072"/>
    <text class="callout" x="1075" y="634">Volume-down control key</text>
    <path class="leader" d="M1000 631 H1072"/>
    <text class="callout" x="819" y="651">Microphone</text>
    <path class="leader" d="M835 616 V641"/>

    <rect class="spec-box" x="805" y="744" width="420" height="124" rx="18"/>
    <text class="spec-heading" x="812" y="770">SPECIFICATION</text>
    <text class="spec-item" x="812" y="791">FREQUENCY RESPONSE: 20-20KHZ</text>
    <text class="spec-item" x="812" y="812">SENSITIVITY: 105±3DB</text>
    <text class="spec-item" x="812" y="833">THD: &lt;3%</text>
    <text class="spec-item" x="812" y="854">CORD LENGTH: 3.6FT</text>
    <text class="spec-heading" x="1021" y="770">CONTENTS</text>
    <text class="spec-item" x="1021" y="787">2 PAIRS OF SWITCHABLE CAPS</text>
    <text class="spec-item" x="1021" y="803">3 PAIRS OF SILICONE EAR TIPS</text>
    <text class="spec-item" x="1021" y="820">USER MANUAL</text>
  </g>

  <!-- base band -->
  <g class="base-info">
    <text class="model-number" x="253" y="967" textLength="213" lengthAdjust="spacing">Model Number : SC-1</text>
    <text class="platform-name" x="507" y="965">Nexo</text>
    <text class="platform-name" x="555" y="965">Kora</text>
    <text class="platform-name" x="604" y="965">Vell</text>
  </g>
</svg>
</body>
</html>
```